Castastrophe General Contractor needs leave behind for sales

Will respond quickly to designer inquires
Fast winning selection
Will notify all of winning selection

Catastrophe Restoration General Contractor offering specialized services to the insurance industry. Sales meeting leave behind flyer for presentation to insurance agents. We would like for agents to refer policyholders to our company for complete residential and commercial restoration projects.

Some copy uploaded for reference. 5.5" x 8.5" approx - double sided color w/ sales business card reproduced on back side. Approved / Preferred Contractor for Brightshield, Vantacover, KRPQ & Fenlo insurance companies.

Larkmoor Company is a general contractor specialized in the restoration industry for both residential and commercial properties.
We have incorporated the best technology tools and partnered with a network of industry professionals across the country to provide the most efficient and comprehensive service available.
Website under construction: www.thelarkmoorcompany.example

Target Market(s)

Insurance Sale Agents

Industry/Entity Type

Residential

Requirements
Must have
• Brightshield, Vantacover & KRPQ & Halvey Dresmit logos. Space to reproduce business card on back.. Looking for concept deign where we can work w/ local designer if necessary to finalize. Open to different sized flyer dependent on design.

```html
<!DOCTYPE html>
<html lang="en">
<head>
<meta charset="utf-8">
<title>Larkmoor Company – Agent Support Flyer</title>
<link rel="stylesheet" href="https://fonts.googleapis.com/css2?family=PT+Sans:wght@400;700&family=Tinos:wght@400;700&display=swap">
<style>
  :root {
    --page-bg: #e7e3dc;
    --blue: #2f7296;
    --blue-deep: #1f5878;
    --blue-light: #4a8fb3;
    --gold: #e3ac3c;
    --gold-deep: #c9922a;
    --white: #ffffff;
    --ink: #1d1d1d;
    --header-grey: #ececec;
    --brand-blue: #1d5b8a;
  }
  * { box-sizing: border-box; margin: 0; padding: 0; }
  html, body { width: 1200px; height: 817px; overflow: hidden; }
  body { background: var(--page-bg); position: relative; font-family: "Tinos", "Times New Roman", serif; }
  h1, h2, h3 { font-weight: 400; }

  .sheet {
    position: absolute; top: 28px; width: 470px; height: 760px; overflow: hidden;
    background: radial-gradient(circle at 60% 55%, var(--blue-light) 0%, var(--blue) 45%, var(--blue-deep) 100%);
    box-shadow: 0 6px 18px rgba(0,0,0,.25);
  }
  .sheet--front { left: 90px; }
  .sheet--back { left: 640px; }

  .sheet__corner { position: absolute; left: 0; top: 0; }

  .top-band { position: absolute; left: 0; top: 0; width: 100%; height: 47px; }
  .top-band__tab { position: absolute; left: 0; top: 0; width: 42px; height: 47px; background: var(--gold); }
  .top-band__phone {
    position: absolute; left: 52px; top: 2px; font-size: 40px; font-weight: 700;
    color: rgba(255,255,255,.09); white-space: nowrap; letter-spacing: 1px;
  }

  .header {
    position: absolute; left: 0; width: 100%;
    background: linear-gradient(to bottom, var(--white), var(--header-grey));
  }
  .sheet--front .header { top: 47px; height: 110px; }
  .sheet--back .header { top: 47px; height: 68px; }

  .brand { position: absolute; left: 14px; top: 14px; width: 150px; text-align: center; }
  .brand__mark { display: block; width: 34px; height: 34px; margin: 0 auto 6px; background: var(--brand-blue); }
  .brand__name { font-size: 13px; color: var(--brand-blue); letter-spacing: .5px; white-space: nowrap; }
  .brand__trades { font-size: 12.5px; color: var(--ink); margin-top: 1px; white-space: nowrap; }

  .header__title {
    position: absolute; right: 2px; top: 26px; width: 290px; text-align: center;
    font-size: 26px; line-height: 31px; color: var(--ink);
  }
  .sheet--back .header__title { left: 50px; top: 14px; right: auto; width: auto; font-size: 31px; text-align: left; }

  .photo {
    position: absolute; border: 5px solid var(--white);
    box-shadow: 0 4px 10px rgba(0,0,0,.35);
  }
  .photo--house { left: 48px; top: 252px; width: 200px; height: 130px; transform: rotate(-8deg);
    background: linear-gradient(to bottom, #b8cde0, #d9dcd9 55%, #8d8f86); }
  .photo--roofer { left: 225px; top: 175px; width: 168px; height: 108px; transform: rotate(-3deg);
    background: linear-gradient(to bottom, #6f6b66, #9c8a7a 60%, #c9c4bb); }
  .photo--tile { left: 210px; top: 292px; width: 205px; height: 128px; transform: rotate(5deg);
    background: linear-gradient(to bottom, #6fa9d6, #c97a4f 40%, #b0603b); }

  .headline {
    position: absolute; left: 0; top: 438px; width: 100%; text-align: center;
    font-family: "PT Sans", Arial, sans-serif; font-weight: 700; font-size: 23px; line-height: 25px;
    color: var(--white); letter-spacing: .2px;
  }
  .tagline {
    position: absolute; left: 57px; top: 503px; width: 384px; height: 31px;
    background: var(--white); border-radius: 3px; box-shadow: 0 2px 5px rgba(0,0,0,.3);
    font-size: 16px; line-height: 31px; text-align: center; color: var(--ink);
  }
  .services { position: absolute; left: 108px; top: 565px; }
  .services__title {
    font-family: "PT Sans", Arial, sans-serif; font-weight: 700; font-size: 16px; color: var(--gold);
    display: flex; align-items: center; gap: 5px; margin-bottom: 6px;
  }
  .services__list { list-style: none; }
  .services__list li { color: var(--white); font-size: 14px; line-height: 24px; white-space: nowrap; }
  .services__list li::before { content: "• "; }

  .badge { position: absolute; background: var(--white); }
  .badge--preferred { left: 294px; top: 693px; width: 101px; height: 37px; }
  .badge--accredited { left: 411px; top: 672px; width: 49px; height: 80px; border: 3px solid var(--brand-blue); }

  .benefit { position: absolute; left: 36px; width: 402px; }
  .benefit__bar {
    height: 23px; background: var(--gold); border-radius: 2px; padding-left: 12px;
    font-size: 14px; line-height: 23px; color: var(--ink); box-shadow: 0 1px 3px rgba(0,0,0,.25);
  }
  .benefit__list { list-style: none; margin: 9px 0 0 10px; }
  .benefit__list li { color: rgba(255,255,255,.9); font-size: 12px; line-height: 16.5px; white-space: nowrap; }
  .benefit__list li::before { content: "• "; }
  .benefit--satisfaction { top: 135px; }
  .benefit--efficiency { top: 236px; }
  .benefit--quality { top: 335px; }

  .partners {
    position: absolute; left: 17px; top: 458px; width: 432px;
    display: grid; grid-template-columns: repeat(3, 139px); grid-auto-rows: 92px; column-gap: 7px; row-gap: 30px;
  }
  .partner {
    background: linear-gradient(to bottom, #ffffff, #ececec); box-shadow: 0 2px 5px rgba(0,0,0,.3);
    display: flex; align-items: center; justify-content: center; gap: 7px;
    font-family: "PT Sans", Arial, sans-serif; font-weight: 700; font-size: 17px; color: var(--brand-blue);
  }
  .partner__square { width: 16px; height: 16px; background: var(--brand-blue); }
  .partner__seal { width: 72px; height: 72px; border-radius: 50%; background: var(--brand-blue); }
  .partner__seal--gold { background: var(--gold-deep); }
</style>
</head>
<body>

<section class="sheet sheet--front" aria-label="Front of flyer">
  <svg class="sheet__corner" width="470" height="760" viewBox="0 0 470 760" aria-hidden="true">
    <path d="M0 450 Q20 680 190 760 L0 760 Z" fill="var(--gold)"/>
  </svg>

  <div class="top-band"><div class="top-band__tab"></div><div class="top-band__phone">(555) 4-Repair</div></div>

  <header class="header">
    <div class="brand">
      <span class="brand__mark"></span>
      <div class="brand__name">LARKMOOR COMPANY</div>
      <div class="brand__trades">Roofing • Siding • Gutters</div>
    </div>
    <h1 class="header__title">Catastrophe Restoration<br>Specialists</h1>
  </header>

  <div class="photo photo--house" role="img" aria-label="Photo of a restored two-storey house"></div>
  <div class="photo photo--roofer" role="img" aria-label="Photo of a roofer on a ladder at a roof edge"></div>
  <div class="photo photo--tile" role="img" aria-label="Photo of a clay tile roof under blue sky"></div>

  <h2 class="headline">PREFERRED CONTRACTOR<br>AGENT SUPPORT</h2>
  <p class="tagline">Providing claims support during and after a CAT event</p>

  <div class="services">
    <h3 class="services__title">
      <svg width="15" height="13" viewBox="0 0 15 13" aria-hidden="true"><path d="M1 7 L5 11 L14 1" fill="none" stroke="var(--gold)" stroke-width="3"/></svg>
      AGENT SUPPORT SERVICES
    </h3>
    <ul class="services__list">
      <li>Guaranteed next day inspections from time of notification</li>
      <li>Damage status reporting directly back to Agent</li>
      <li>Assist policy holder in filing claim to CAT desk</li>
    </ul>
  </div>

  <div class="badge badge--preferred" role="img" aria-label="Halvey Dresmit preferred contractor badge"></div>
  <div class="badge badge--accredited" role="img" aria-label="Accredited business badge"></div>
</section>

<section class="sheet sheet--back" aria-label="Back of flyer">
  <div class="top-band"><div class="top-band__tab"></div><div class="top-band__phone">(555) 4-Repair</div></div>

  <header class="header"><h1 class="header__title">Agent Benefits</h1></header>

  <div class="benefit benefit--satisfaction">
    <h3 class="benefit__bar">Greater Satisfaction, Increased Retention</h3>
    <ul class="benefit__list">
      <li>Increase policyholder satisfaction</li>
      <li>Demonstrate a greater commitment to customer satisfaction</li>
      <li>Follow up on outcome beyond the closing of a claim</li>
    </ul>
  </div>
  <div class="benefit benefit--efficiency">
    <h3 class="benefit__bar">Enhanced Efficiency</h3>
    <ul class="benefit__list">
      <li>Increase efficiency in moving from claim to restoration completion</li>
      <li>“In-house” systems closely linked to the insurer or administrator</li>
      <li>Shorten the timeline from claims settlement to finished repairs</li>
    </ul>
  </div>
  <div class="benefit benefit--quality">
    <h3 class="benefit__bar">Increased Quality</h3>
    <ul class="benefit__list">
      <li>Pre-screened and credentialed for license, insurance, and financial stability</li>
      <li>Monitored performance and control standards for higher-quality outcomes</li>
      <li>Background verification on all staff and field representatives</li>
    </ul>
  </div>

  <div class="partners">
    <div class="partner">Fenlo</div>
    <div class="partner" role="img" aria-label="Certified roofing inspector seal"><span class="partner__seal partner__seal--gold"></span></div>
    <div class="partner">KRPQ</div>
    <div class="partner"><span class="partner__square"></span>Brightshield</div>
    <div class="partner" role="img" aria-label="Restoration contractors association seal"><span class="partner__seal"></span></div>
    <div class="partner">Vantacover</div>
  </div>
</section>

</body>
</html>
```